Brochure/flyer for Tuftmoor Nappy Company

My Business name is Plover Wrenlyn Nappies
I am wanting a A4 size brochure (Flyer) to be folded twice. Measurements when folded 210 x 99 mm
I am just about to launch my Modern Cloth Nappy Products and i am wanting a brochure to target new mum's who aren't familiar with Modern cloth nappies and also for mums who are familiar with modern cloth nappies but are looking at trying my brand.
I want the Brochure to be very informative but yet Simple to read. I want people to feel like they want to buy my nappies after they read my Brochure.
The Brochure can be reworded and additional information can be added if you feel its needed, But i would like all the information listed below to be on the brochure.

MOTO: Cloth Nappies The Modern Way

The nappy design is designed in Australia and Australian Owned.

WHY USE CLOTH?
-Save thousands of Dollars
-Easy to use
-Looks Cute
-Super Absorbency
It costs approximately $3000 to use disposable nappies on a child from birth until 2 and a half years, that is Approximately 6000 nappies going into Landfill. This is based on a child going through 6-8 nappies per day.
Modern cloth nappies, on the other hand, cost around $500 for a full stash of 24 nappies. This allows for the child to wear 6-8 nappies per day with a load of nappies going in the wash every 2-3 days. As we have a range of nappies that are one-size-fits-most for bubs ranging from 3kg to 18kg, that $500 would cover your complete stash from birth right through to toilet training, Not to mention the money you would save by using the nappies again for any subsequent Children you may have.
Eliminates your baby's exposure to harmful Chemicals that can be in disposable nappies.
The manufacturing and use of disposable nappies can amount to 2-3 times more wasted water than using cloth nappies
Using Disposable Nappies fill up our landfill, Disposable nappies take more than 100 years to decompose, possibly up to 500 years.

PRODUCTS AVAILABLE:
Newborn: All in One (AIO) Fits approx 2-7kg
Velcro All in Two, One size Fits Most (OSFM) fits approx 3 to 18kg
Snap All in Two, One size Fits Most (OSFM) Fits Approx 3 to 18kg
Extra Inserts
Wetbags
Bamboo Biodegradable liners

The Materials used and features:
All in 2 Nappy (AI2):
Outer Shell Features- A waterproof TPU shell to keep all the wetness in.
Lining is a made of Microfleece material which is soft on baby's skin and Wicks moisture away from the baby's skin it is also very fast drying
Double leg Gussets to avoids any potential side leg Leaks
a poo guard at the back to reduce any leaks from occurring up the back
Insert is Made from 70% Bamboo and 30% Organic Cotton, The extra trim insert with extra absorbency qualities that can easily be double up for a heavy wetting baby or for an all night solution.

Insert snaps in and out Which is easy to remove and replace
A Pocket opening is also available to add a Booster in for long naps or for night time use. Insert is 2 layers sewn together and then folded twice to create 6 layers of absorbency. Unsnap insert from shell for washing, As there is not 3 layers sewn together like most inserts, it dries much quicker and washes more thoroughly, therefore less chance of smells accumulating

Why are these inserts so great?
– Super soft and silky
– Very breathable
– Naturally Anti-bacterial
– Absorbs 3 to 4 times more than cotton
– Doesn't feel sticky or uncomfortable when wet

The newborn nappy has a TPU waterproof Shell and is a all in one (AIO), has 4 layers of absorbency of 70% Bamboo and 30% Organic Cotton, With Microfleece lining which is super soft on newborns delicate skin.
The newborn nappy has a snap to hold down the front of the nappy where the umbilical cord will be for the first week or so. there is also snaps to adjust the size that little bit smaller for Premature babies or small babies. There is also double leg gussets to avoid any leaks around the legs. There is also a Poo guard at the back to avoid any leaks coming up from the back. The waist has a cross over snap for a extra small waist

PRICING:
One Size Fits Most:
Velcro: $25.95
Snap: $25.95
All In One Newborn:
$19.95

PACKAGES:
Price Depends on What nappies you choose for your package

Trial 3 pack: 5% Discount
6 Pack: 10% Discount
12 Pack: 15% Discount
24 Pack: 20% discount

Extra Inserts $7.00
Wetbags: $10
Bamboo Biodegradable Liners: $10
Contact Details:
Jolene Pridmore
Phone: 0491730284
E-mail: ploverwrenlynnappies@mailzenbox.com
Socialnook: www.socialnookhub.com/PloverWrenlynNappies

I have changed a few things on the brief so please read carefully before changing or making another design,

Thanks :) 

Target Market(s)

Mums and Dads, care takers, Guardians and grandparents

Industry/Entity Type

Baby

Requirements
Must have
• Must have the Logo and picture i have sent but you are welcome to put other pictures of babies but please do not put pictures of babies with disposable nappies on. and if you are going to put pics of babies i would prefer the pictures not to show how the Velcro or snaps look at the front of the nappy. for example: put pictures that show the nappy side on or from the back. You could put pictures of babies or of nature etc "saving the Environment"
Should not have
• no pictures of other cloth nappy brands No disposable nappies

```html
<!DOCTYPE html>
<html lang="en">
<head>
<meta charset="utf-8">
<title>Plover Wrenlyn Nappies – Brochure</title>
<link rel="stylesheet" href="https://fonts.googleapis.com/css2?family=Andika:wght@400;700&family=Delius&family=Jost:wght@500;600&display=swap">
<style>
  :root {
    --plum: #7d3f8e;
    --orchid: #9b4a9e;
    --body-ink: #474048;
    --rule: #d6b4da;
    --pink-top: #dc95c6;
    --pink-mid: #a9489b;
    --pink-low: #e6c6e0;
    --lilac-wash: #efe3f1;
    --white: #ffffff;
  }
  * { box-sizing: border-box; margin: 0; padding: 0; }
  html, body { width: 1200px; height: 852px; overflow: hidden; background: #fff; }
  .brochure {
    position: relative; width: 1200px; height: 852px; display: flex;
    font-family: "Andika", sans-serif;
  }
  .panel { position: relative; height: 100%; }

  /* Inside panel: insert benefits */
  .panel--details {
    width: 395px;
    background: linear-gradient(180deg, #fbf8fb 0%, #f7f2f7 70%, #efe2ef 100%);
  }
  .details__title {
    position: absolute; left: 47px; top: 44px;
    font-family: "Jost", sans-serif; font-weight: 600; font-size: 16.5px; color: var(--plum);
  }
  .benefits {
    position: absolute; left: 35px; top: 72px; width: 328px; height: 159px;
    border: 1px solid var(--rule); border-radius: 8px; background: var(--white);
    padding: 3px 10px 0 12px; list-style: none;
    font-size: 15.5px; line-height: 25.3px; color: var(--body-ink);
  }
  .benefits li::before { content: "•"; color: var(--orchid); margin-right: 5px; }
  .details__copy {
    position: absolute; left: 47px; top: 236px; width: 308px;
    font-size: 15.6px; line-height: 25.4px; color: var(--body-ink);
  }
  .details__rule {
    position: absolute; left: 132px; top: 648px; width: 124px; height: 1px; background: #d9cbd9;
  }
  .art-blossom {
    position: absolute; left: 0; top: 690px; width: 180px; height: 162px;
    border-radius: 0 90px 0 0;
    background: radial-gradient(circle at 20% 80%, #b06ab0 0%, #d7a6d6 45%, rgba(239,226,239,0) 80%);
  }
  .art-baby {
    position: absolute; left: 225px; top: 655px; width: 125px; height: 150px; border-radius: 50%;
    background: radial-gradient(ellipse at center, #f6d9e6 0%, #e9c7e2 55%, rgba(247,242,247,0) 75%);
  }

  /* Middle panel: pricing & contact */
  .panel--pricing {
    width: 400px; color: var(--white);
    background: linear-gradient(180deg, var(--pink-top) 0%, #c26cb2 30%, var(--pink-mid) 52%, #c27cb6 72%, var(--pink-low) 100%);
  }
  .pricing { position: absolute; left: 40px; top: 42px; width: 300px; font-size: 16.5px; line-height: 24px; }
  .pricing__heading { font-family: "Jost", sans-serif; font-weight: 600; font-size: 21px; line-height: 28px; margin-bottom: 2px; }
  .pricing__heading--gap { margin-top: 10px; }
  .pricing__note { color: #f2cfe7; line-height: 22px; width: 275px; }
  .packages { margin-top: 12px; display: grid; grid-template-columns: 101px auto; line-height: 22px; }
  .extras { margin-top: 16px; line-height: 22px; }

  .contact {
    position: absolute; left: 420px; top: 480px; width: 348px; height: 198px;
    border-radius: 12px; background: rgba(255,255,255,0.72);
    padding: 6px 14px 0; color: var(--plum); font-size: 16px; line-height: 24.5px;
  }
  .contact__label { font-family: "Jost", sans-serif; font-weight: 600; font-size: 17px; }
  .contact__label--title { text-decoration: underline; }
  .contact__name { font-family: "Delius", sans-serif; font-size: 21px; line-height: 30px; }
  .contact a { color: var(--plum); text-decoration: none; }
  .contact__web { font-size: 14px; letter-spacing: -0.2px; white-space: nowrap; }

  .brand-small {
    position: absolute; left: 442px; top: 725px; display: flex; align-items: center; gap: 12px;
    font-family: "Delius", sans-serif; font-size: 27px; color: #7a3c86;
  }
  .brand-dot { width: 52px; height: 52px; border-radius: 50%; background: #a4529f; flex: none; }

  /* Front cover */
  .panel--cover {
    width: 405px;
    background: linear-gradient(180deg, #fdfbfd 0%, var(--lilac-wash) 45%, #f7f2f7 75%, #fff 100%);
  }
  .brand-main {
    position: absolute; left: 0; top: 90px; width: 405px;
    display: flex; flex-direction: column; align-items: center; gap: 26px;
  }
  .brand-main .brand-dot { width: 150px; height: 150px; }
  .brand-main__name { font-family: "Delius", sans-serif; font-size: 37px; color: #6f3a86; }
  .cover__motto {
    position: absolute; left: 0; top: 390px; width: 405px; text-align: center;
    font-family: "Andika", sans-serif; font-weight: 400; font-size: 34px; line-height: 48px; color: var(--orchid);
  }
  .cover__sub {
    position: absolute; left: 0; top: 492px; width: 405px; text-align: center;
    font-family: "Delius", sans-serif; font-size: 19px; color: var(--plum);
  }
  .cover__photo {
    position: absolute; left: 0; top: 655px; width: 405px; height: 197px;
    background: linear-gradient(90deg, #ede7e6 0%, #e4c9b8 25%, #f0d5c6 55%, #efeae8 80%, #f8f6f5 100%);
  }
</style>
</head>
<body>
<main class="brochure">
  <section class="panel panel--details">
    <h2 class="details__title">Why are these inserts so great?</h2>
    <ul class="benefits">
      <li>Super soft and silky</li>
      <li>Very breathable</li>
      <li>Naturally Anti-bacterial</li>
      <li>Absorbs 3 to 4 times more than cotton</li>
      <li>Doesn't feel sticky or uncomfortable when wet</li>
    </ul>
    <p class="details__copy">The newborn nappy has a TPU waterproof shell and is a all in one (AIO), has 4 layers of absorbency of 70% Bamboo and 30% Organic Cotton, With Microfleece lining which is super soft on newborns delicate skin.<br>The newborn nappy has a snap to hold down the front of the nappy where the umbilical cord will be for the first week or so. There is also snaps to adjust the size that little bit smaller for premature babies or small babies. Featuring double leg gussets to avoid any leaks around the legs. A poo guard at the back to avoid any leaks coming up from the back. The waist has a cross over snap for a extra small waist.</p>
    <div class="details__rule"></div>
    <div class="art-blossom" role="img" aria-label="Large soft purple blossom decoration"></div>
    <div class="art-baby" role="img" aria-label="Cartoon baby wearing a blue cloth nappy"></div>
  </section>

  <section class="panel panel--pricing">
    <div class="pricing">
      <h2 class="pricing__heading">Pricing:</h2>
      <p>One Size Fits Most:</p>
      <p>• Velcro: $25.95</p>
      <p>• Snap: $25.95</p>
      <p>All In One Newborn: $19.95</p>
      <h2 class="pricing__heading pricing__heading--gap">Packages:</h2>
      <p class="pricing__note">Price depends on what nappies you choose for your package.</p>
      <div class="packages">
        <span>Trial 3 pack:</span><span>5% Discount</span>
        <span>6 Pack:</span><span>10% Discount</span>
        <span>12 Pack:</span><span>15% Discount</span>
        <span>24 Pack:</span><span>20% discount</span>
      </div>
      <div class="extras">
        <p>Extra Inserts: $7.00</p>
        <p>Wetbags: $10</p>
        <p>Bamboo Biodegradable Liners: $10</p>
      </div>
    </div>
  </section>

  <div class="contact">
    <p class="contact__label contact__label--title">Contact Details:</p>
    <p class="contact__name">Jolene Pridmore</p>
    <p><span class="contact__label">Phone:</span> 0491730284</p>
    <p class="contact__label">E-mail:</p>
    <p><a href="mailto:ploverwrenlynnappies@mailzenbox.com">ploverwrenlynnappies@mailzenbox.com</a></p>
    <p class="contact__label">Socialnook:</p>
    <p class="contact__web">www.socialnookhub.com/PloverWrenlynNappies</p>
  </div>

  <div class="brand-small"><span class="brand-dot"></span><span>Plover Wrenlyn</span></div>

  <section class="panel panel--cover">
    <div class="brand-main">
      <span class="brand-dot"></span>
      <span class="brand-main__name">Plover Wrenlyn</span>
    </div>
    <h1 class="cover__motto">Cloth Nappies The<br>Modern Way</h1>
    <p class="cover__sub">Australian Owned And Designed</p>
    <div class="cover__photo" role="img" aria-label="Photo of a newborn baby lying on a soft white blanket"></div>
  </section>
</main>
</body>
</html>
```